Marwick Ostrand Law website for a law firm

modern clean website for a small boutique law firm. Based in Sacramento, CA and the Bay Area. Practice areas of Family Law, Civil litigation, and Criminal Defense. We already have a logo design as well as attorney pictures to include on page.
Would like images of California included on site.
Would like site to go with Logo that is already designed...blue/grey/white colors.

Industry/Entity Type

Law Firm

Number of Pages Required

5+ page

Requirements
Must have
• I already have several pages of content drafted. Just need the pages with images to input content. Must be clean and modern feel. Want it to reflect California and small boutique feel that is provided personalized legal attention.
• Must have a page where I can blog or post articles on.

```html
<!DOCTYPE html>
<html lang="en">
<head>
<meta charset="utf-8">
<title>Divorce | Marwick Ostrand Law</title>
<link href="https://fonts.googleapis.com/css2?family=Open+Sans:wght@300;400;600;700&family=Playfair+Display:wght@600&display=swap" rel="stylesheet">
<style>
  :root {
    --blue: #3b80c3;
    --navy: #2a2a5a;
    --red: #e01b1b;
    --ink: #1c1c1c;
    --page: #f9f9fc;
    --footer: #a3a3a3;
    --field: #c6c6c6;
    --white: #ffffff;
    --rule: #ece4c8;
  }
  * { margin: 0; padding: 0; box-sizing: border-box; }
  html, body { width: 736px; height: 1200px; overflow: hidden; background: var(--white); }
  body { position: relative; font-family: "Open Sans", sans-serif; color: var(--ink); }

  .site-header { position: absolute; top: 0; left: 0; width: 736px; height: 86px; background: var(--white); border-bottom: 1px solid var(--rule); }
  .phone { position: absolute; top: 13px; left: 583px; display: flex; align-items: center; gap: 6px; color: var(--red); font-weight: 700; font-size: 11.5px; }
  .brand { position: absolute; top: 40px; left: 15px; font-weight: 300; font-size: 33px; letter-spacing: 1px; color: var(--blue); }
  .main-nav { position: absolute; top: 60px; left: 343px; display: flex; gap: 12px; font-size: 11.5px; font-weight: 600; color: var(--blue); }
  .main-nav .sep { font-weight: 400; }
  .main-nav .current { color: var(--navy); }

  .hero { position: absolute; top: 86px; left: 0; width: 736px; height: 155px;
    background:
      radial-gradient(ellipse 55% 70% at 50% 100%, #6b7fd0 0%, #8d95d0 45%, rgba(170,160,200,0) 75%),
      linear-gradient(180deg, #c6b4b9 0%, #c3aebd 45%, #b7a4b7 65%, #4d63bf 88%, #233c98 100%); }
  .hero h1 { position: absolute; top: 69px; width: 100%; text-align: center; font-family: "Playfair Display", serif; font-weight: 600; font-size: 23px; letter-spacing: 2.5px; color: var(--white); }

  .content { position: absolute; top: 241px; left: 0; width: 736px; height: 763px; background: var(--page); }
  .block { position: absolute; left: 128px; width: 468px; }
  .block p, .block li { font-size: 8.6px; line-height: 13.9px; }
  .block h2 { font-size: 14px; font-weight: 600; color: var(--blue); letter-spacing: 0.2px; margin-bottom: 13px; }
  .block p + p.gap { margin-top: 13.9px; }
  .block ul { list-style: none; margin-left: 35px; }
  .block li { position: relative; padding-left: 15px; }
  .block li::before { content: "•"; position: absolute; left: 0; font-size: 7px; }

  .site-footer { position: absolute; top: 1004px; left: 0; width: 736px; height: 175px; background: var(--footer); color: var(--white); }
  .footer-nav { position: absolute; top: 30px; left: 64px; height: 100px; border-left: 1px solid var(--white); padding-left: 13px; }
  .footer-nav a { display: block; font-size: 8.6px; line-height: 22px; color: var(--white); text-decoration: none; }
  .help-title { position: absolute; top: 30px; left: 199px; font-size: 11px; font-weight: 600; }
  .field { position: absolute; left: 317px; width: 104px; height: 17px; background: var(--field); border: 1px solid #d8d8d8; font-size: 4.5px; color: #8a8a8a; padding: 3px 5px; }
  .field.message { left: 438px; top: 29px; width: 104px; height: 79px; }
  .send { position: absolute; left: 438px; top: 123px; width: 104px; height: 18px; border: 1px solid #d6d6d6; font-size: 7.5px; font-weight: 600; letter-spacing: 0.8px; text-align: center; line-height: 16px; color: #e4e4e4; }
  .connect { position: absolute; top: 30px; left: 644px; font-size: 11px; font-weight: 600; }
  .social { position: absolute; top: 54px; left: 646px; display: flex; gap: 5.5px; }
</style>
</head>
<body>
  <header class="site-header">
    <div class="phone">
      <svg width="13" height="13" viewBox="0 0 14 14" aria-hidden="true">
        <circle cx="7" cy="7" r="6.2" fill="none" stroke="#666" stroke-width="0.9"/>
        <path d="M4.6 3.8 L5.8 3.6 L6.4 5.2 L5.6 5.9 Q6.3 7.6 8.1 8.4 L8.8 7.6 L10.4 8.2 L10.2 9.4 Q9.6 10.2 8.6 10 Q4.6 9 4 5.4 Q3.9 4.4 4.6 3.8 Z" fill="none" stroke="#666" stroke-width="0.8"/>
      </svg>
      <span>123-456-7890</span>
    </div>
    <div class="brand">MOLAW</div>
    <nav class="main-nav">
      <span>HOME</span><span class="sep">|</span>
      <span>ABOUT</span><span class="sep">|</span>
      <span class="current">PRACTICE AREAS</span><span class="sep">|</span>
      <span>CONTACT</span><span class="sep">|</span>
      <span>BLOG</span>
    </nav>
  </header>

  <section class="hero" role="img" aria-label="Snow-capped California mountain peak at dusk under a pink sky">
    <h1>DIVORCE</h1>
  </section>

  <main class="content">
    <div class="block" style="top:42px">
      <p>Your life will undergo manychanges upon the dissolution of your marriage. The steps you take during this pivotal period can have a substantial impact on your future. Marwick &amp; Ostrand Law is a dedicated family law firm that can help you reach the most equitable possible divorce settlement. Our partners have a strong litigation background with years of experience in civil and criminal trials, which makes us both strategic negotiators and aggressive courtroom advocates. Our legal counsel focuses on reaching your goals while helping to ease the stress of this difficult process.</p>
    </div>

    <section class="block" style="top:133px">
      <h2>Divorce Mediation</h2>
      <p>Divorce mediation is often an effective means of obtaining a divorce final judgment. The process involves a trained mediator who guides the parties toward agreement. At the end of mediation, you sign an agreement that sets forth terms of child custody, child support, spousal support and disposition of assets and debts.</p>
      <p>Our attorney remains an integral part of the process. We prepare you before mediation and develop a comprehensive strategy to reach your goals. During mediation, we act as your advocates to protect your rights and pursue an equitable settlement. We often recommend mediation to:</p>
      <ul>
        <li>Reduce the stress of contentious court proceedings</li>
        <li>Lower costs of obtaining a divorce</li>
        <li>Reach final judgment sooner</li>
        <li>Make important decisions rather than allowing the court to decide</li>
        <li>Build a foundation for cooperation with the other parent</li>
      </ul>
    </section>

    <section class="block" style="top:340px">
      <h2>Divorce Trial</h2>
      <p>Sometimes, issues cannot be resolved through mediation. For example, one parent may not be willing to concede child custody that would be in the best interest for the child. Likewise, spouses may not be able to settle on the best means of dividing the house. In cases involving domestic violence, mediation may be frightening and unfair to the victim of the abuse.</p>
      <p class="gap">Our attorneys have substantial trial experience and are always ready to take the case to litigation to achieve a better outcome. By negotiating most of the issues in advance, we canconcentrate our efforts on the contested issues before the court. When we decide to proceed with litigation, we will explain the court proceedings to you so you can feel confident and prepared. We understand that this is a difficult process and we will fight for you and your family at every stage.</p>
    </section>

    <section class="block" style="top:534px">
      <h2>Divorce Discovery and Trial Preparation</h2>
      <p>California law requires both parties to disclose important information about assets, debts, income and other financial matters. In addition, we collect evidence that supports your position on child custody, parenting plans, child support, spousal support and division of your property.</p>
      <p>Our attorneys are effective, efficient, confidential and respectful as we guide you through the discovery process. If necessary, we will challenge attempts by your spouse to hide assets or to be overly intrusive into your finances or personal life.</p>
    </section>

    <section class="block" style="top:672px">
      <h2>Get the Representation You Need During Your Divorce</h2>
      <p>Marwick &amp; Ostrand Law helps you meet your goals in divorce regarding child custody, child support, spousal support, parenting plans, visitation and property disposition. Schedule an appointment at our Sacramento or Bay Area offices.</p>
    </section>
  </main>

  <footer class="site-footer">
    <nav class="footer-nav">
      <a>Home</a><a>About Us</a><a>Contact Us</a><a>Practice Areas</a><a>Blog</a>
    </nav>
    <div class="help-title">Looking for Help?</div>
    <div class="field" style="top:30px">Your name</div>
    <div class="field" style="top:60px">Your Email Address</div>
    <div class="field" style="top:92px">Your phone no.</div>
    <div class="field message">Your message</div>
    <div class="send">SEND</div>
    <div class="connect">CONNECT</div>
    <svg class="social" width="46" height="12" viewBox="0 0 46 12" aria-hidden="true">
      <circle cx="5.5" cy="6" r="5.5" fill="#2b2b2b"/>
      <circle cx="23" cy="6" r="5.5" fill="#2b2b2b"/>
      <circle cx="40.5" cy="6" r="5.5" fill="#2b2b2b"/>
    </svg>
  </footer>
</body>
</html>
```